Business cards for Remote DBA team

Business cards for team offering database administration, consultation, machine learning and AI services. As of now team is using both
www.korvilnet.cz and www.brestmoorlab.cz URLs

Target Market(s)

IT managers

Industry/Entity Type

It Professional

Contact Information for Business Card

Should include logo
name, email, phone, twitter tag

Font styles to use
Sans Serif

Colors

Designer to choose colors to be used in the design.

```html
<!DOCTYPE html>
<html lang="en">
<head>
<meta charset="utf-8">
<title>Brestmoor Lab – Business Card</title>
<link rel="stylesheet" href="https://fonts.googleapis.com/css2?family=Arimo:wght@400;700&display=swap">
<style>
  :root {
    --card-white: #ffffff;
    --brand-blue: #1e88c7;
    --panel-blue-light: #2a9bd6;
    --panel-blue-dark: #136fae;
    --accent-green: #5aac4b;
    --text-white: #ffffff;
  }
  html, body {
    margin: 0;
    padding: 0;
    width: 1200px;
    height: 720px;
    overflow: hidden;
    background: var(--card-white);
  }
  .card {
    position: relative;
    width: 1200px;
    height: 720px;
    overflow: hidden;
    background: var(--card-white);
    font-family: "Arimo", Arial, sans-serif;
  }
  .card-panel {
    position: absolute;
    inset: 0;
    width: 1200px;
    height: 720px;
  }
  .brand {
    position: absolute;
    left: 80px;
    top: 262px;
  }
  .brand-mark {
    position: absolute;
    left: 8px;
    top: 22px;
    width: 72px;
    height: 72px;
    border-radius: 50%;
    background: var(--brand-blue);
  }
  .brand-name {
    position: absolute;
    left: 101px;
    top: 0;
    margin: 0;
    font-weight: 700;
    font-size: 44px;
    line-height: 46px;
    color: var(--brand-blue);
    white-space: nowrap;
  }
  .brand-tagline {
    position: absolute;
    left: 80px;
    top: 411px;
    margin: 0;
    font-size: 16.5px;
    color: var(--brand-blue);
    white-space: nowrap;
  }
  .person {
    position: absolute;
    left: 653px;
    top: 102px;
    color: var(--text-white);
  }
  .person-name {
    margin: 0;
    font-weight: 700;
    font-size: 34px;
    letter-spacing: 0.5px;
  }
  .person-role {
    margin: 16px 0 0;
    font-size: 19px;
  }
  .contacts {
    position: absolute;
    left: 651px;
    top: 333px;
    margin: 0;
    padding: 0;
    list-style: none;
    color: var(--text-white);
    font-size: 28px;
  }
  .contact-item {
    display: flex;
    align-items: center;
    height: 38px;
    white-space: nowrap;
  }
  .contact-item + .contact-item { margin-top: 16px; }
  .contact-item.social { margin-top: 47px; }
  .contact-icon {
    display: inline-flex;
    width: 26px;
    justify-content: center;
    margin-right: 4px;
    font-size: 26px;
  }
  .social-dot {
    width: 22px;
    height: 22px;
    border-radius: 50%;
    background: var(--text-white);
  }
  .websites {
    position: absolute;
    left: 654px;
    top: 557px;
    margin: 0;
    color: var(--text-white);
    font-size: 28px;
    letter-spacing: 1.4px;
    line-height: 39px;
  }
</style>
</head>
<body>
  <main class="card">
    <svg class="card-panel" viewBox="0 0 1200 720" role="img" aria-label="Blue panel with a faded photo of technology hexagons and a hand">
      <defs>
        <linearGradient id="panelBlue" x1="0" y1="0" x2="1" y2="1">
          <stop offset="0" stop-color="var(--panel-blue-light)"/>
          <stop offset="0.6" stop-color="#1a86c6"/>
          <stop offset="1" stop-color="var(--panel-blue-dark)"/>
        </linearGradient>
      </defs>
      <path class="panel-edge" d="M632 0 C470 170 395 430 538 720 L1200 720 L1200 0 Z" fill="var(--accent-green)"/>
      <path class="panel-body" d="M650 0 C505 175 425 440 570 720 L1200 720 L1200 0 Z" fill="url(#panelBlue)"/>
    </svg>

    <div class="brand">
      <span class="brand-mark"></span>
      <p class="brand-name">BRESTMOOR<br>LAB</p>
    </div>
    <p class="brand-tagline">Big Data and Machine Learning Experts</p>

    <header class="person">
      <h1 class="person-name">TOMAS HALEK</h1>
      <p class="person-role">Data Engineer</p>
    </header>

    <ul class="contacts">
      <li class="contact-item phone">
        <span class="contact-icon">
          <svg width="24" height="30" viewBox="0 0 24 30" aria-hidden="true">
            <path d="M6 2 L10 2 L11 9 L8 11 C9 16 11 20 14 23 L17 21 L22 25 L20 29 C12 29 3 18 3 8 C3 5 4 3 6 2 Z" fill="var(--text-white)"/>
          </svg>
        </span>: +420 735 218 604
      </li>
      <li class="contact-item email"><span class="contact-icon">@</span>: Tomas@brestmoorlab.cz</li>
      <li class="contact-item social"><span class="contact-icon"><span class="social-dot"></span></span>: socialnet.cz/tomashalek</li>
    </ul>

    <p class="websites">www.korvilnet.cz<br>www.brestmoorlab.cz</p>
  </main>
</body>
</html>
```